Sales sheet for printing and embroidery apparel items - Copper Fern Prints

I would like a one page flyer or sales sheet that I would use as a template to send different images of apparel we produce. I have attached examples of layouts I like.
- Ideally, it would have space for 3-5 items.
- I would like it one page only - not a folding flyer.
- Our companies name is Copper Fern Prints.
- This will be used for many different products and markets so I don't need wording/copy. You can use wording from the 7Q7 or K81 flyer.

Colors
0054AA
0677BA
7BADD7
CADEEF
E8F1F8
00AB8E
00BBA5
67D7C9
C6EFE9
E9F9F6
FFC000
F8CF3A
FAE287
FDF2CF
FEFAEE

Requirements
Must have
• Places for between 3 and 5 images of apparel (t-shirts, hats etc)

```html
<!DOCTYPE html>
<html lang="en">
<head>
<meta charset="utf-8">
<title>Copper Fern Prints – Sales Sheet</title>
<link rel="stylesheet" href="https://fonts.googleapis.com/css2?family=Oswald:wght@600;700&family=Montserrat:wght@400;500;600;700&family=Caveat:wght@500&display=swap">
<style>
  :root {
    --navy: #173d6d;
    --orange: #e5704a;
    --orange-dark: #b94a2a;
    --paper: #fbfbfa;
    --backdrop: #bcbdbf;
    --ink: #1c1c1c;
    --white: #ffffff;
  }
  * { margin: 0; padding: 0; box-sizing: border-box; }
  html, body { width: 1200px; height: 1200px; overflow: hidden; background: var(--backdrop); }
  .sheet {
    position: absolute; left: 175px; top: 0;
    width: 849px; height: 1200px;
    background: var(--paper);
    overflow: hidden;
    font-family: "Montserrat", sans-serif;
  }
  .hero-art {
    position: absolute; left: 470px; top: 0; width: 379px; height: 414px;
    background: radial-gradient(ellipse at 60% 45%, #dcdde0 0%, #e8e9ea 45%, rgba(251,251,250,0) 80%);
  }
  .headline {
    position: absolute; left: 50px; top: 72px; width: 580px;
    font-family: "Oswald", sans-serif; font-weight: 700;
    font-size: 66px; line-height: 71px; color: var(--navy);
    letter-spacing: -0.5px; white-space: nowrap;
  }
  .brand-mark { position: absolute; left: 641px; top: 68px; width: 165px; text-align: center; }
  .brand-square { width: 113px; height: 101px; margin: 0 auto 8px; background: var(--navy); }
  .brand-name {
    font-weight: 700; font-size: 20px; line-height: 23px;
    color: var(--navy); text-transform: uppercase;
  }
  .tagline {
    position: absolute; left: 50px; top: 314px;
    font-size: 21px; line-height: 31px; color: var(--ink);
  }
  .intro-band {
    position: absolute; left: 0; top: 414px; width: 849px; height: 235px;
    background: var(--navy); color: var(--white);
  }
  .intro-band h2 {
    position: absolute; left: 50px; top: 23px;
    font-weight: 500; font-size: 30px; line-height: 40px; white-space: nowrap;
  }
  .intro-copy {
    position: absolute; left: 50px; top: 122px; width: 290px;
    font-size: 13.5px; line-height: 18.5px;
  }
  .intro-divider {
    position: absolute; left: 352px; top: 120px; width: 1px; height: 76px; background: var(--orange);
  }
  .feature-list {
    position: absolute; left: 373px; top: 118px; list-style: none;
    font-size: 11.3px; font-weight: 600; line-height: 21.2px; white-space: nowrap;
  }
  .feature-list li::before {
    content: ""; display: inline-block; width: 5px; height: 5px; border-radius: 50%;
    background: var(--orange); margin-right: 7px; vertical-align: 2px;
  }
  .offer-title {
    position: absolute; left: 203px; top: 676px;
    font-family: "Caveat", cursive; font-weight: 500; font-size: 44px;
    color: var(--orange); line-height: 50px;
    border-bottom: 1.5px solid var(--orange); padding: 0 2px;
  }
  .product { position: absolute; top: 720px; height: 229px; border-radius: 14px; }
  .product--hoodie { left: 46px; width: 174px; background: linear-gradient(160deg, #2a2a2a, #101010); }
  .product--cap { left: 236px; width: 177px; top: 750px; height: 199px; border-radius: 80px 80px 20px 20px; background: linear-gradient(180deg, #2b2b2b, #121212); }
  .product--tee { left: 418px; width: 197px; top: 728px; height: 221px; background: linear-gradient(170deg, #1d2f63, #142350); }
  .product--patch { left: 629px; width: 174px; top: 764px; height: 172px; border-radius: 18px; background: linear-gradient(135deg, #2a2a2e, #151517); }
  .service-band {
    position: absolute; left: 0; top: 961px; width: 849px; height: 53px;
    background: var(--orange); color: var(--white);
    padding-left: 50px; font-size: 20px; font-weight: 500; line-height: 53px; white-space: nowrap;
  }
  .service-band .sep { color: var(--orange-dark); margin: 0 4px; }
  .footer-mark { position: absolute; left: 48px; top: 1079px; width: 82px; height: 72px; background: var(--navy); }
  .footer-invite { position: absolute; left: 150px; top: 1082px; width: 360px; color: var(--navy); }
  .footer-invite h3 { font-weight: 500; font-size: 20px; line-height: 25px; white-space: nowrap; }
  .footer-invite p { font-size: 14.5px; line-height: 18px; margin-top: 5px; }
  .contact { position: absolute; left: 543px; top: 1074px; width: 262px; color: var(--navy); white-space: nowrap; }
  .contact-label { font-weight: 700; font-size: 13.5px; line-height: 18px; }
  .contact-phone { font-weight: 700; font-size: 37px; line-height: 44px; color: var(--orange); }
  .contact-links { font-size: 13.5px; line-height: 18px; }
</style>
</head>
<body>
  <main class="sheet">
    <div class="hero-art" role="img" aria-label="Faint misty mountain landscape with a standing stag silhouette"></div>

    <h1 class="headline">Custom Apparel for<br>Your Brand, Team,<br>or Campaign</h1>

    <div class="brand-mark">
      <div class="brand-square"></div>
      <div class="brand-name">Copper Fern<br>Prints</div>
    </div>

    <p class="tagline">Traditional craftmanship. Premium Printing.<br>Reliable fulfillment.</p>

    <section class="intro-band">
      <h2>We help organizations create apparel that<br>looks professional and feels worth wearing.</h2>
      <p class="intro-copy">Copper Fern Prints works with schools, alumni programs, businesses, events, and teams to produce custom apparel with quality, consistency, and care.</p>
      <div class="intro-divider"></div>
      <ul class="feature-list">
        <li>Premium screen printing and embroidery</li>
        <li>Flexible apparel options for different markets</li>
        <li>Helpful art support and proofing</li>
        <li>Shipping and fulfillment solutions available</li>
      </ul>
    </section>

    <h2 class="offer-title">What we offer:</h2>

    <div class="product product--hoodie" role="img" aria-label="Black hoodie with a red and white printed graphic"></div>
    <div class="product product--cap" role="img" aria-label="Black trucker cap with gold embroidered lettering"></div>
    <div class="product product--tee" role="img" aria-label="Navy t-shirt with a printed floating astronaut graphic"></div>
    <div class="product product--patch" role="img" aria-label="Square black embroidered patch with a colorful splatter mascot"></div>

    <div class="service-band">Custom T-Shirts<span class="sep">-</span>Premium Embroidery<span class="sep">-</span>Headwear<span class="sep">-</span>Patches<span class="sep">-</span>Fulfillment</div>

    <div class="footer-mark"></div>
    <div class="footer-invite">
      <h3>We’d love to work with you!</h3>
      <p>Contact Copper Fern Prints to start your<br>next apparel project today.</p>
    </div>

    <div class="contact">
      <div class="contact-label">CONTACT COPPER FERN PRINTS:</div>
      <div class="contact-phone">555-014-2738</div>
      <div class="contact-links">cfprints.com &nbsp;// &nbsp;info@cfprints.com</div>
    </div>
  </main>
</body>
</html>
```